84k | SOLUTIONS Biz Card Design

Brightmoor Solutions, LLC
84k | HOME INSPECTIONS
84k | ENVIRONMENTAL TESTING
84k | THERMOGRAPHY IMAGING
(Would like progressive design, maybe use 84k as a logo or part of logo; want to reflect healthy environments, incorporating sun, or blue skies, etc.; primary colors, one side or two is acceptable)
Updates

I'm very partial to the simple modern fonts such as Helvetica or Museo Sans 500 or the new one I've recently seen that's like Helvetica with attitude. Added Tuesday, May 5, 2015

Target Market(s)

Home owners and realtors

Industry/Entity Type

Progressive

Contact Information for Business Card

Ned Forsythe, President/CEO
NedForsythe@84kSolutions.example
www.84kSolutions.example
555.730.4418
555.730.4419 fax

Font styles to use
Other font styles liked:
• Fabrica, Helvetica, Arial, Nevis, Nexa

Colors
0355a3
ec1f27
ffffff
fbed22
ffc214
9bcb3b

Requirements
Must have
• Professional yet bright colors design. Don't want to look too mom and pop.
Nice to have
• Use '84k' to create a logo.
Should not have
• Not too busy, make two-sided if there's not enough white space.

```html
<!DOCTYPE html>
<html lang="en">
<head>
<meta charset="utf-8">
<title>84k Solutions Business Card</title>
<link href="https://fonts.googleapis.com/css2?family=Arimo:wght@400;700&display=swap" rel="stylesheet">
<style>
  :root {
    --page: #e9e9ec;
    --card: #23262f;
    --facet: #2f323c;
    --blue: #0355a3;
    --blue-deep: #0a4d99;
    --white: #ffffff;
    --gold: #ffc214;
    --rule: #8a8d96;
  }
  * { box-sizing: border-box; margin: 0; padding: 0; }
  html, body { width: 1200px; height: 1000px; overflow: hidden; }
  body {
    background: var(--page);
    font-family: "Arimo", Arial, sans-serif;
    color: var(--white);
    position: relative;
  }
  .card {
    position: absolute;
    left: 250px;
    width: 700px;
    height: 400px;
    background: var(--card);
    overflow: hidden;
    box-shadow: 0 10px 28px rgba(0,0,0,.22);
  }
  .card--front { top: 65px; }
  .card--back { top: 535px; }
  .card svg.shape { position: absolute; inset: 0; }

  .brand { position: absolute; display: flex; align-items: center; gap: 14px; }
  .brand-dot { width: 22px; height: 22px; border-radius: 50%; background: var(--gold); flex: none; }
  .brand-name { font-size: 30px; font-weight: 700; color: var(--white); white-space: nowrap; }

  .card--front .brand { left: 56px; top: 130px; }
  .divider-v { position: absolute; left: 330px; top: 80px; width: 1px; height: 200px; background: var(--rule); }
  .services { position: absolute; left: 372px; top: 118px; list-style: none; font-size: 25px; line-height: 44px; }
  .services li::before { content: "•"; margin-right: 12px; }
  .front-url { position: absolute; left: 40px; bottom: 22px; font-size: 20px; font-weight: 700; color: var(--white); }

  .person { position: absolute; left: 44px; top: 44px; }
  .person-name { font-size: 36px; font-weight: 700; }
  .person-title { font-size: 14px; margin-top: 6px; }
  .card--back .brand { right: 44px; top: 110px; }
  .divider-h { position: absolute; left: 300px; right: 44px; top: 190px; height: 1px; background: var(--gold); }
  .contacts { position: absolute; right: 44px; top: 218px; list-style: none; font-size: 20px; line-height: 34px; text-align: right; }
  .contacts li { display: flex; justify-content: flex-end; align-items: center; gap: 12px; }
  .contacts svg { width: 20px; height: 20px; flex: none; }
</style>
</head>
<body>

<section class="card card--front" aria-label="Business card front">
  <svg class="shape" viewBox="0 0 700 400" width="700" height="400" aria-hidden="true">
    <path d="M0 262 C 150 300, 380 360, 480 400 L0 400 Z" fill="var(--blue)"/>
  </svg>
  <div class="brand"><span class="brand-dot"></span><span class="brand-name">84k Solutions</span></div>
  <div class="divider-v"></div>
  <ul class="services">
    <li>Home Inspections</li>
    <li>Environmental Testing</li>
    <li>Thermography Imaging</li>
  </ul>
  <p class="front-url">www.84kSolutions.example</p>
</section>

<section class="card card--back" aria-label="Business card back">
  <svg class="shape" viewBox="0 0 700 400" width="700" height="400" aria-hidden="true">
    <path d="M0 0 L300 0 L0 400 Z" fill="var(--facet)"/>
    <path d="M0 0 L150 0 L0 80 Z" fill="var(--blue)"/>
  </svg>
  <div class="person">
    <p class="person-name">Ned Forsythe</p>
    <p class="person-title">President/CEO</p>
  </div>
  <div class="brand"><span class="brand-dot"></span><span class="brand-name">84k Solutions</span></div>
  <div class="divider-h"></div>
  <ul class="contacts">
    <li>555.730.4418
      <svg viewBox="0 0 24 24" aria-label="phone"><path fill="#fff" d="M6.6 10.8a15 15 0 0 0 6.6 6.6l2.2-2.2c.3-.3.7-.4 1-.2 1.1.4 2.3.6 3.6.6.6 0 1 .4 1 1V20c0 .6-.4 1-1 1A17 17 0 0 1 3 4c0-.6.4-1 1-1h3.5c.6 0 1 .4 1 1 0 1.3.2 2.5.6 3.6.1.3 0 .7-.2 1z"/></svg>
    </li>
    <li>555.730.4419
      <svg viewBox="0 0 24 24" aria-label="fax"><path fill="#fff" d="M7 3h8l2 2v4H7zM4 10h16a1 1 0 0 1 1 1v8a1 1 0 0 1-1 1H4a1 1 0 0 1-1-1v-8a1 1 0 0 1 1-1zm3 3v2h2v-2zm4 0v2h2v-2zm4 0v2h2v-2z"/></svg>
    </li>
    <li>NedForsythe@84kSolutions.example
      <svg viewBox="0 0 24 24" aria-label="email"><path fill="#fff" d="M3 5h18v14H3zm2 2v.5l7 5 7-5V7zm0 3v7h14v-7l-7 5z"/></svg>
    </li>
    <li>www.84kSolutions.example
      <svg viewBox="0 0 24 24" aria-label="website"><circle cx="12" cy="12" r="9" fill="none" stroke="#fff" stroke-width="2"/><path d="M3 12h18M12 3c3 3 3 15 0 18M12 3c-3 3-3 15 0 18" fill="none" stroke="#fff" stroke-width="1.6"/></svg>
    </li>
  </ul>
</section>

</body>
</html>
```